Lantern - Web Design Project

We are seeking to have our website redesigned. Our current webpage is rather dated looking www.lantern-outcomes.com We will be utilizing similar content to explain our services as what is in the website now. We do not see it at a retail portal but rather a website for those inquiring about our services as a reference check so to speak.

We wish to have a look that is considered clean, fresh, contemporary and contains a business savvy vibe.

We prefer isolated white background and also wish to retain the integrity of our Logo and colour scheme.

We are looking for something that doesnt look like it was designed at home on sitemoose. We are hoping to find something that looks like it would reside on a tablet.
Updates

Hello designers!

We apologize for our tardiness as we have been quite preoccupied. We will be extending our invites to the end of January!

Hello All,

Please review our offer once again for updated requirements.  We are hoping to accept a design by months end.

Lantern

Target Market(s)

Business to business clients and Large manufacturers

Industry/Entity Type

Retail

Requirements
Must have
• Existing Logo

There must be an area dedicated to an intro video that will be incorporated on our landing page.

We require design of the other pages as well not only the landing page.

```html
<!DOCTYPE html>
<html lang="en">
<head>
<meta charset="utf-8">
<title>Lantern Performance Group</title>
<link href="https://fonts.googleapis.com/css2?family=PT+Sans:wght@400;700&family=Oswald:wght@400;500&display=swap" rel="stylesheet">
<style>
:root{
  --red:#e8383c;
  --red-dark:#c8272b;
  --ink:#3a3a3a;
  --text:#444;
  --muted:#888;
  --dark:#222;
  --line:#ddd;
  --soft:#f7f7f7;
  --white:#fff;
}
*{margin:0;padding:0;box-sizing:border-box}
html,body{width:1158px;height:1200px;overflow:hidden;background:var(--white)}
body{position:relative;font-family:"PT Sans",sans-serif;color:var(--text);font-size:13px}
a{color:inherit;text-decoration:none}
.topline{position:absolute;left:0;top:0;width:1158px;height:4px;background:var(--red)}
.social{position:absolute;top:0;left:882px;display:flex;gap:5px}
.social span{width:39px;height:42px;background:#c9c9c9;display:flex;align-items:center;justify-content:center;clip-path:polygon(0 0,100% 0,100% 82%,50% 100%,0 82%)}
.social span.home{background:var(--red)}
.brand{position:absolute;left:107px;top:34px;display:flex;align-items:center;gap:8px}
.brand-dot{width:16px;height:16px;border-radius:50%;background:var(--red)}
.brand-name{font-size:44px;font-weight:400;color:#555;letter-spacing:-1px;line-height:1}
.lang{position:absolute;left:627px;top:78px;font-size:12.5px;color:#555}
.lang .on{color:var(--red)}
.lang i{font-style:normal;margin:0 6px;color:#888}
.search{position:absolute;left:790px;top:70px;width:226px;height:31px;border:1px solid var(--line);font-size:11.5px;font-style:italic;color:#999;padding:8px 8px}
.search-btn{position:absolute;left:1024px;top:70px;width:28px;height:31px;border:1px solid var(--line);display:flex;align-items:center;justify-content:center}
.nav{position:absolute;left:107px;top:117px;width:945px;height:33px;background:#3b3b3b;border-radius:3px;overflow:hidden}
.nav-red{position:absolute;left:0;top:0;width:695px;height:33px;background:linear-gradient(#ec4548,var(--red-dark));clip-path:polygon(0 0,665px 0,695px 33px,0 33px)}
.nav ul{position:absolute;left:19px;top:0;list-style:none;display:flex;gap:36px;line-height:33px;color:var(--white);font-size:14px;font-weight:700}
.nav .call{position:absolute;right:30px;top:0;line-height:33px;color:#eee;font-size:19px}
.video{position:absolute;left:107px;top:169px;width:666px;height:298px;border-radius:3px;overflow:hidden;background:linear-gradient(#9fb0c0 0%,#d8dde2 35%,#4f7d97 55%,#5b6b5a 70%,#6a6a66 100%)}
.play{position:absolute;left:302px;top:42px;width:62px;height:62px;border-radius:50%;background:rgba(20,20,20,.55);border:3px solid var(--white);display:flex;align-items:center;justify-content:center}
.play-label{position:absolute;left:0;top:112px;width:100%;text-align:center;color:var(--white);font-size:13px;font-weight:700;letter-spacing:.5px;text-shadow:0 1px 2px rgba(0,0,0,.5)}
.caption{position:absolute;left:0;bottom:0;width:100%;height:95px;background:rgba(30,30,30,.78);color:var(--white);padding:10px 18px}
.caption h3{font-weight:400;font-size:18px;margin-bottom:6px}
.caption p{font-size:13px;line-height:21px;padding-left:3px;width:640px}
.dots{position:absolute;right:12px;top:11px;display:flex;gap:6px}
.dots b{width:13px;height:13px;border-radius:50%;background:var(--white)}
.dots b:first-child{background:var(--red)}
.login{position:absolute;left:791px;top:169px;width:261px;height:297px;border-radius:3px;background:linear-gradient(#1e1e1e,#3a3a3a 62%,#262626 62%);color:var(--white);text-align:center}
.login h3{font-family:"Oswald",sans-serif;font-weight:400;font-size:18px;text-align:left;padding:14px 0 0 24px;display:flex;align-items:center;gap:6px}
.field{margin:13px auto 0;width:209px;height:24px;background:#f2f2f2;color:#999;text-align:left;font-size:13px;padding:4px 14px}
.field+.field{margin-top:11px}
.remember{margin-top:12px;font-size:13px;color:#eee}
.remember b{display:inline-block;width:11px;height:11px;background:#ddd;vertical-align:-1px;margin-right:6px}
.forgot{font-size:13px;color:#eee;margin-top:3px}
.btn{display:inline-block;background:linear-gradient(#f04a4d,var(--red-dark));color:var(--white);font-weight:700;border-radius:3px}
.btn-login{margin-top:10px;width:82px;height:30px;line-height:30px;font-size:17px}
.login h4{font-family:"Oswald",sans-serif;font-weight:400;font-size:17px;margin-top:10px}
.btn-open{margin-top:8px;width:178px;height:32px;line-height:32px;font-size:17px}
.box{position:absolute;left:108px;width:665px;border:3px double #ccc;background:var(--soft);padding:12px 17px}
.box h2{font-weight:400;font-size:21px;color:var(--ink);margin-bottom:6px}
.box p{font-size:13.5px;line-height:23px;margin-bottom:23px}
.box p:last-child{margin-bottom:0}
.more{color:var(--red)}
.welcome{top:497px;height:249px}
.who{top:766px;height:297px}
.side{position:absolute;left:791px;width:261px;border-radius:4px;box-shadow:0 1px 4px rgba(0,0,0,.25);background:var(--white);overflow:hidden}
.side h3{height:38px;background:linear-gradient(#444,#111);color:var(--white);font-weight:400;font-size:19px;padding:7px 18px}
.services{top:486px;height:363px}
.services ul{list-style:none;padding:4px 12px 0}
.services li{height:35px;line-height:35px;border-bottom:1px dashed var(--line);font-size:13.5px;padding-left:23px;position:relative}
.services li:last-child{border:0}
.services li::before{content:"";position:absolute;left:9px;top:13px;border-left:5px solid #444;border-top:4px solid transparent;border-bottom:4px solid transparent}
.contact{top:868px;height:194px}
.contact address{font-style:normal;font-size:13.5px;line-height:21px;padding:15px 20px}
.contact .red{color:var(--red)}
.footer{position:absolute;left:0;top:1093px;width:1158px;height:107px;background:var(--dark);color:var(--white);text-align:center;font-size:13px}
.footer nav{margin-top:28px}
.footer nav a.on{color:var(--red)}
.footer nav i{font-style:normal;margin:0 12px}
.footer p{margin-top:12px}
.footer u{text-decoration:underline}
</style>
</head>
<body>
<div class="topline"></div>
<div class="social">
  <span class="home"><svg width="22" height="18" viewBox="0 0 22 18"><path d="M11 1 1 9h3v8h5v-5h4v5h5V9h3z" fill="#fff"/></svg></span>
  <span aria-label="Social link"></span>
  <span aria-label="Social link"></span>
  <span aria-label="Social link"></span>
</div>
<div class="brand"><span class="brand-dot"></span><span class="brand-name">Lantern</span></div>
<div class="lang"><span class="on">English</span><i>|</i>Français<i>|</i>Sign In</div>
<div class="search">Search here...</div>
<div class="search-btn"><svg width="14" height="14" viewBox="0 0 14 14"><circle cx="5.5" cy="5.5" r="4" fill="none" stroke="#333" stroke-width="2"/><path d="M8.5 8.5 13 13" stroke="#333" stroke-width="2.4"/></svg></div>
<div class="nav">
  <div class="nav-red"></div>
  <ul><li>Who We Are</li><li>Cross The Lantern</li><li>Performance Solutions</li><li>Sustain Solutions</li><li>Join Us</li></ul>
  <div class="call">Call us: 1-888-410-2736</div>
</div>
<div class="video" role="img" aria-label="Intro video area: still of a cyclist riding a coastal road beside the sea under a cloudy sky, with a play button">
  <div class="play"><svg width="24" height="26" viewBox="0 0 24 26"><path d="M3 1 23 13 3 25z" fill="#fff"/></svg></div>
  <div class="play-label">Watch our intro video</div>
  <div class="caption">
    <h3>Marta Kellaway</h3>
    <p>"There are managers so preoccupied with their e-mail messages that they never look up from their screens to see what's happening in the nondigital world."</p>
    <div class="dots"><b></b><b></b><b></b><b></b></div>
  </div>
</div>
<div class="login">
  <h3><svg width="20" height="20" viewBox="0 0 20 20"><circle cx="10" cy="6" r="5" fill="#fff"/><path d="M0 20c0-6 4-8 10-8s10 2 10 8z" fill="#fff"/></svg>CUSTAMER LOGIN</h3>
  <div class="field">User name</div>
  <div class="field">Password</div>
  <div class="remember"><b></b>Remember me</div>
  <div class="forgot">Forget your password</div>
  <span class="btn btn-login">Log in</span>
  <h4>Not a member?</h4>
  <span class="btn btn-open">Open an account</span>
</div>
<section class="box welcome">
  <h2>Welcome to Lantern Performance Group</h2>
  <p>Lantern Performance Group Inc. is the leading provider of profit generating and people development solutions. With the hands-on experience of best practices, the state-of-the-art technology and in-depth information we help companies increase their efficiencies and profits. Frank, honest, committed, valuable and rewarding are words that customers use to describe the quality services provided by Lantern Performance Group.</p>
  <p>Learn more about us, or find the right solutions for your specific business.We will be delighted to help you achieve better business results.</p>
</section>
<section class="box who">
  <h2>Who We Are</h2>
  <p>With highly experienced performance consultants, trainers and subject matter experts based throughout the North America, Europe, the Middle East and Asia Pacific we offer unrivalled skills and expertise in designing and implementing highly interactive and proven performance solutions, aimed at developing your people and rapidly delivering increased sales and profits.</p>
  <p>We do not believe that a cookie cutter approach works in today's environment and that's why we utilize our expertise, people knowledge and various tools to provide a number of customized business solutions.</p>
  <p>We will assist you in driving towards improved sales, customer loyalty, performance indicators, processes,<br><a class="more">Read More »</a></p>
</section>
<aside class="side services">
  <h3>Our Services</h3>
  <ul>
    <li>Business Diagnostics</li><li>Executive Coaching</li><li>Management Development</li><li>Talent Management</li><li>Creating Sales Culture</li><li>Creating Customer Loyalty</li><li>Performance Improvement Initiatives</li><li>Finance &amp; Insurance Training</li><li>Product Launches</li>
  </ul>
</aside>
<aside class="side contact">
  <h3>Contact Details</h3>
  <address>Lantern Performance Group<br>482 Harbourview Rd, Eastwick,<br>NB E2K 7P1, Canada<br><br>Telephone: +1.888.410.2736<br>Email: <span class="red">info@lantern-outcomes.com</span></address>
</aside>
<footer class="footer">
  <nav><a class="on">Home</a><i>|</i>Who We Are<i>|</i>Cross The Lantern<i>|</i>Performance Solutions<i>|</i>Sustain Solutions<i>|</i>Join Us<i>|</i>Site map<i>|</i>Privacy Policy</nav>
  <p>Copyright © 2013 <u>lantern-outcomes.com</u> . All Right Reserved</p>
</footer>
</body>
</html>
```